LANDING PAGE on a Word Press platform.

I have a website, www.thequietharborledger.com and need to create a new landing page. I purchased a new url, www.quietharborledger.com and set it up on Word Press. It has a theme (I was trying to do it myself, but gave up) but you can change it if you need to. I will give you access so you can work directly on the Word Press Platform. Please visit my site, www.thequietharborledger, so you can see what we are selling.
Updates

Thank you for being so patient. Unfortunately I had some pressing personal problems and had to leave the country for a couple of weeks. I am back now and will choose a design today. Thank you again!

Target Market(s)

Stock Market, High Worth Individuals, Traders, Investors

Requirements
Must have
• My landing page must look very professional and rich. I am sending a copy of my logo but the "the" before The Quiet Harbor Ledger, needs to be removed. Some testimonials and services we provide. (all found on my home page)
Nice to have
• I am open to a new color scheme if possible. The logo colors would have to be changed.
Should not have
• Should not be too busy with too many images or text. I want a clean and easy to read landing page

```html
<!DOCTYPE html>
<html lang="en">
<head>
<meta charset="utf-8">
<title>The Quiet Harbor Ledger</title>
<link href="https://fonts.googleapis.com/css2?family=Oswald:wght@500&family=Roboto:ital,wght@0,400;0,500;0,700;1,400&display=swap" rel="stylesheet">
<style>
:root{
  --navy:#1b4585;
  --navy-deep:#153a72;
  --gold:#c9961a;
  --red:#d51c1c;
  --ink:#2b2b2b;
  --text:#444;
  --muted:#777;
  --grey-band:#f1f1f1;
  --link:#1d7fc4;
  --white:#fff;
}
*{box-sizing:border-box;margin:0;padding:0}
html,body{width:812px;height:1200px;overflow:hidden}
body{font-family:'Roboto',sans-serif;color:var(--text);background:var(--white)}
.page{width:812px;height:1200px;position:relative}
.wrap{width:572px;margin:0 auto;position:relative}

.site-header{height:63px}
.site-header .wrap{height:63px}
.brand{position:absolute;left:0;top:12px;display:flex;align-items:center;gap:8px}
.brand-mark{width:38px;height:38px;border-radius:50%;background:var(--navy)}
.brand-name{font-weight:700;font-size:16px;line-height:17px;color:var(--navy);width:120px}
.social-top{position:absolute;right:0;top:13px;display:flex;gap:5px}
.social-top span{width:17px;height:17px;border-radius:50%;display:block}
.call{position:absolute;right:0;top:33px;font-weight:700;font-size:15px;color:var(--ink)}
.call b{color:var(--gold)}

.hero{height:276px;position:relative}
.hero-visual{position:absolute;inset:0;background:radial-gradient(ellipse at 45% 40%,#2a6aa8 0%,#1c4f8c 45%,#12396e 100%)}
.signup{position:absolute;left:513px;top:14px;width:178px;height:248px;background:#eaf1f8;box-shadow:0 2px 6px rgba(0,0,0,.3)}
.signup-head{background:var(--gold);height:58px;text-align:center;color:var(--white);padding-top:8px}
.signup-head h2{font-family:'Oswald',sans-serif;font-weight:500;font-size:30px;line-height:30px;letter-spacing:.5px}
.signup-head p{font-size:7px;font-weight:500;margin-top:4px}
.signup form{padding:12px 12px 0}
.field{display:block;width:100%;height:22px;border:1px solid #cfd8e2;background:var(--white);font-size:7.5px;color:#777;padding:6px 8px;margin-bottom:4px}
.field.msg{height:48px}
.try{display:block;width:100%;height:33px;margin-top:4px;background:linear-gradient(#e52525,#c41212);border:0;color:var(--white);font:700 14px 'Roboto',sans-serif}

.intro{height:127px;text-align:center;padding-top:22px}
.sec-title{font-size:15px;font-weight:400;color:var(--ink)}
.sec-title b{font-weight:700}
.intro p{font-size:9px;line-height:16px;color:var(--text);margin-top:9px}

.steps{height:202px;background:var(--grey-band);text-align:center;padding-top:24px}
.step-list{display:flex;justify-content:space-between;margin-top:26px}
.step{width:150px}
.step svg{height:40px;width:50px}
.step h3{font-size:11px;font-weight:500;color:var(--ink);margin-top:4px}
.step p{font-size:8.5px;line-height:13.5px;color:var(--muted);margin-top:4px}

.results{height:214px;text-align:center;padding-top:19px}
.results p{font-size:8.5px;line-height:16.3px;color:var(--ink)}
.results .p1{margin-top:15px}
.results .p2{margin-top:16px}
.btn-more{display:inline-block;margin-top:13px;background:var(--navy);color:var(--white);font-size:10px;width:86px;height:21px;line-height:21px}

.clients{height:242px;background:var(--grey-band);text-align:center;padding-top:30px}
.quotes{display:flex;justify-content:space-between;margin-top:18px;text-align:left}
.quote{width:280px;height:125px;background:var(--white);border:2px solid #d3d4e2;padding:13px 12px}
.quote p{font-style:italic;font-size:8px;line-height:15.5px;color:var(--ink)}
.quote .who{font-size:7.5px;color:var(--link);margin-top:6px}
.quote .role{font-size:7.5px;font-weight:700;color:var(--gold);margin-top:3px}
.dots{display:flex;justify-content:center;gap:6px;margin-top:18px}
.dots span{width:10px;height:10px;border-radius:50%;background:#c8c8c8}
.dots span.on{background:var(--navy)}

.site-footer{height:76px;background:var(--navy-deep);color:var(--white)}
.site-footer .wrap{height:76px}
.foot-links{position:absolute;left:0;top:24px;font-size:7.5px;display:flex;gap:13px}
.copy{position:absolute;left:0;top:42px;font-size:7px}
.news{position:absolute;left:240px;top:18px}
.news h4{font-size:10.5px;font-weight:400}
.news-row{display:flex;gap:5px;margin-top:6px}
.news-row .in{width:132px;height:19px;background:var(--white);color:#888;font-size:7.5px;padding:5px 7px}
.news-row .go{width:49px;height:19px;background:var(--red);font-size:8.5px;text-align:center;line-height:19px}
.follow{position:absolute;right:0;top:18px;text-align:right}
.follow h4{font-size:10.5px;font-weight:400}
.follow-icons{display:flex;gap:7px;margin-top:9px}
.follow-icons span{width:18px;height:18px;border:1.5px solid var(--white);border-radius:50%}
</style>
</head>
<body>
<div class="page">
  <header class="site-header">
    <div class="wrap">
      <div class="brand"><span class="brand-mark"></span><span class="brand-name">The Quiet Harbor Ledger</span></div>
      <div class="social-top" aria-label="Social links">
        <span style="background:#2b5ca8"></span><span style="background:#29a3dc"></span><span style="background:#d9503f"></span><span style="background:#c4302b"></span>
      </div>
      <div class="call"><b>Call Now:</b> 877-555-0143</div>
    </div>
  </header>

  <section class="hero">
    <div class="hero-visual" role="img" aria-label="Smiling trader in a blue shirt and tie presenting a rising stock chart on a blue background"></div>
    <div class="wrap">
      <div class="signup">
        <div class="signup-head"><h2>SIGN UP NOW</h2><p>START A 2-WEEK FREE TRIAL TODAY!</p></div>
        <form>
          <div class="field">Name</div>
          <div class="field">Email Address</div>
          <div class="field">Phone Number</div>
          <div class="field msg">Message</div>
          <div class="try">TRY RISK FREE</div>
        </form>
      </div>
    </div>
  </section>

  <section class="intro">
    <div class="wrap" style="width:580px">
      <h2 class="sec-title">The Leader in <b>Stock Trader</b></h2>
      <p>Lorem Ipsum is simply dummy text of the printing and typesetting industry. Lorem Ipsum has been the industry's standard dummy text ever since the 1500s, when an unknown printer took a galley of type and scrambled it to make a type specimen book.<br>It has survived not only five centuries, but also the leap into electronic typesetting, remaining essentially unchanged. It was popularised in the 1960s with the release of Letraset sheets containing Lorem Ipsum passages.</p>
    </div>
  </section>

  <section class="steps">
    <div class="wrap">
      <h2 class="sec-title">Easy Trading <b>Steps</b></h2>
      <div class="step-list">
        <div class="step">
          <svg viewBox="0 0 50 40"><circle cx="25" cy="22" r="16" fill="var(--navy)"/><text x="25" y="29" text-anchor="middle" font-family="Roboto,sans-serif" font-weight="700" font-size="20" fill="#fff">$</text></svg>
          <h3>Competitive Pricing</h3>
          <p>Lorem Ipsum is simply dummy printing and typesetting industry. Lorem Ipsum has been</p>
        </div>
        <div class="step">
          <svg viewBox="0 0 50 40"><path d="M8 20V12h26V5l10 10-10 10v-7H14v2z" fill="var(--navy)"/><path d="M42 20v8H16v7L6 25l10-10v7h20v-2z" fill="var(--navy)"/></svg>
          <h3>Superior Execution</h3>
          <p>Lorem Ipsum is simply dummy printing and typesetting industry. Lorem Ipsum has been</p>
        </div>
        <div class="step">
          <svg viewBox="0 0 50 40" fill="var(--navy)"><rect x="8" y="26" width="5" height="12"/><rect x="16" y="20" width="5" height="18"/><rect x="24" y="23" width="5" height="15"/><rect x="32" y="15" width="5" height="23"/><rect x="40" y="10" width="5" height="28"/><path d="M7 22l10-9 7 5 14-13" stroke="var(--navy)" stroke-width="3" fill="none"/><path d="M33 3h9v9z"/></svg>
          <h3>Actionable Research</h3>
          <p>Lorem Ipsum is simply dummy printing and typesetting industry. Lorem Ipsum has been</p>
        </div>
      </div>
    </div>
  </section>

  <section class="results">
    <div class="wrap" style="width:580px">
      <h2 class="sec-title">QHL Top Ten Recommendations of <b>Q1 2015</b></h2>
      <p class="p1">In the first quarter of 2015, the top ten recommendations had an average return of 74% with KRVX generating the highest return of 193%.<br>In 2015, QHL's Tweets and Current Portfolio generated combined profits of $70,847.</p>
      <p class="p2">In the first quarter of 2015, including open trades, QHL's Current Portfolio had 56 recommendations for a total profit of $23,412. The 56 recommendations had 33 positive trades for a win ratio of 59%. The average return on each trade was 2.36% with an average holding period of 20.06 days.The Tweets Portfolio had 67 recommendations for a total profit of $47,435. The 67 recommendations had 46 correct trades for a win ratio of 69%. The average return on each trade was 9.37% with an average holding period of 5.64 days.</p>
      <a class="btn-more">Know More</a>
    </div>
  </section>

  <section class="clients">
    <div class="wrap">
      <h2 class="sec-title">Satisfied <b>Clients</b></h2>
      <div class="quotes">
        <div class="quote">
          <p>“Lorem Ipsum is simply dummy text of the printing and typesetting industry. Lorem Ipsum has been the industry's standard dummy text ever since the 1500s, when an unknown printer took a galley of type and scrambled it to make a type specimen book. It has survived not</p>
          <div class="who">Nora Whitfield</div><div class="role">Satisfied Client</div>
        </div>
        <div class="quote">
          <p>“Lorem Ipsum is simply dummy text of the printing and typesetting industry. Lorem Ipsum has been the industry's standard dummy text ever since the 1500s, when an unknown printer took a galley of type and scrambled it to make a type specimen book. It has survived not</p>
          <div class="who">Nora Whitfield</div><div class="role">Satisfied Client</div>
        </div>
      </div>
      <div class="dots"><span class="on"></span><span></span><span></span></div>
    </div>
  </section>

  <footer class="site-footer">
    <div class="wrap">
      <nav class="foot-links"><span>About</span><span>Terms &amp; Conditions</span><span>Privacy Policy</span><span>Career</span></nav>
      <div class="copy">Copyright 2015 quietharborledger | All Rights Reserved</div>
      <div class="news"><h4>Newsletter Signup</h4><div class="news-row"><div class="in">Email Address</div><div class="go">Sign Up</div></div></div>
      <div class="follow"><h4>Follow Us</h4><div class="follow-icons" aria-label="Social links"><span></span><span></span><span></span><span></span></div></div>
    </div>
  </footer>
</div>
</body>
</html>
```